VIP Card Design Project

Trodza is a premium sneaker store selling brand name sneakers like Velm, Quorra, Brenvo and etc. ( www.trodzashop.com ) We need to design a VIP card to promote one of our discount program called "Trodza VIP Circle 9", which offers 24% discount off all full-priced items. The idea is because we have a "Pelmor fitness center" (pelmorfitness.com) next door and we are trying to design a discount program for people going to the fitness center.
The design is for the front of the card. The back will be black and white with benefits information and member information.
The front design need to include our logo, "VIP", "Circle 9" and our web address "Trodza.com" and Chatterly and blipster logo.
It will be a plastic card in the size of 3.375x2.125 (bleed size 3.5x2.25)

```html
<!DOCTYPE html>
<html lang="en">
<head>
<meta charset="utf-8">
<title>Trodza VIP Circle 9 Card</title>
<link href="https://fonts.googleapis.com/css2?family=Cinzel:wght@600;700&family=Arimo:wght@400;700&display=swap" rel="stylesheet">
<style>
  :root {
    --green: #2f9e3a;
    --green-dark: #1f7d2b;
    --green-light: #5cbf45;
    --orange: #ef7d1a;
    --tag: #f6e04a;
    --red: #d8262c;
    --ink: #3aa043;
    --paper: #ffffff;
    --backdrop: #ece9e4;
    --string: #9a9a9a;
  }
  * { margin: 0; padding: 0; box-sizing: border-box; }
  html, body { width: 1200px; height: 665px; overflow: hidden; }
  body {
    background: var(--backdrop);
    font-family: "Arimo", Arial, sans-serif;
    position: relative;
  }
  .card {
    position: absolute;
    top: 160px;
    width: 540px;
    height: 340px;
    background: var(--paper);
    border-radius: 8px;
    overflow: hidden;
    box-shadow: 0 6px 18px rgba(0,0,0,.18);
  }
  .card--front { left: 40px; }
  .card--back { left: 620px; }
  .card svg.shapes { position: absolute; inset: 0; width: 100%; height: 100%; }

  /* front */
  .club-title {
    position: absolute; left: 40px; top: 14px;
    font-family: "Cinzel", Georgia, serif; font-weight: 700;
    font-size: 27px; color: var(--paper); letter-spacing: .5px;
  }
  .social { position: absolute; right: 16px; top: 62px; display: flex; gap: 10px; }
  .social__item {
    display: flex; align-items: center; gap: 4px;
    font-size: 10px; font-weight: 700; color: var(--green-dark);
  }
  .social__item::before {
    content: ""; width: 10px; height: 10px; background: var(--green); border-radius: 2px;
  }
  .brand-name {
    position: absolute; left: 0; right: 0; top: 72px; text-align: center;
    font-weight: 700; font-size: 76px; color: var(--green); letter-spacing: 2px;
  }
  .photo {
    position: absolute; border: 2px solid var(--red);
    box-shadow: 0 2px 5px rgba(0,0,0,.3);
  }
  .photo--one { left: 30px; top: 195px; width: 98px; height: 68px;
    background: linear-gradient(135deg, #c9472b, #e9c9a0 55%, #3452a8); }
  .photo--two { left: 215px; top: 168px; width: 90px; height: 64px;
    background: linear-gradient(135deg, #a5875d, #eeeeee 50%, #c83a2b); }
  .photo--three { left: 408px; top: 123px; width: 112px; height: 68px;
    background: linear-gradient(135deg, #3a3a3a, #7b7b7b 45%, #d9382e); }
  .tag {
    position: absolute; width: 40px; height: 48px; background: var(--tag);
    clip-path: polygon(25% 0, 75% 0, 100% 18%, 100% 100%, 0 100%, 0 18%);
    display: flex; flex-direction: column; align-items: center; justify-content: center;
    color: var(--red); font-weight: 700; font-size: 13px; line-height: 1;
  }
  .tag small { font-size: 7px; color: #222; font-weight: 400; margin-top: 2px; }
  .tag--one { left: 158px; top: 232px; }
  .tag--two { left: 352px; top: 198px; }
  .web {
    position: absolute; right: 20px; font-size: 12px; color: var(--paper);
    display: flex; align-items: center; gap: 5px;
  }
  .web::before {
    content: ""; width: 9px; height: 9px; border: 1.5px solid var(--paper); border-radius: 50%;
  }
  .card--front .web { top: 268px; }

  /* back */
  .member-fields { position: absolute; inset: 0; color: var(--paper); font-size: 12px; }
  .member-fields__row { position: absolute; display: flex; align-items: flex-end; gap: 4px; }
  .member-fields__row span.line { display: inline-block; border-bottom: 1px dotted rgba(255,255,255,.8); height: 12px; }
  .member-fields__row--id { right: 20px; top: 38px; }
  .member-fields__row--id .line { width: 85px; }
  .member-fields__row--name { left: 22px; top: 86px; }
  .member-fields__row--name .line { width: 175px; }
  .benefits { position: absolute; left: 22px; top: 124px; right: 28px; color: var(--ink); font-size: 10px; line-height: 1.3; }
  .benefits__title {
    font-family: "Cinzel", Georgia, serif; font-weight: 700; font-size: 15px;
    color: var(--orange); margin-bottom: 2px;
  }
  .benefits ol { list-style: none; margin-top: 4px; }
  .benefits li { position: relative; padding-left: 16px; }
  .benefits li b { position: absolute; left: 0; font-weight: 400; color: var(--orange); }
  .card--back .web { top: 306px; }
</style>
</head>
<body>

<section class="card card--front">
  <svg class="shapes" viewBox="0 0 540 340" preserveAspectRatio="none" aria-hidden="true">
    <path d="M0 0 H540 V40 Q300 52 0 62 Z" fill="var(--green)"/>
    <path d="M0 0 H540 V16 Q300 30 0 40 Z" fill="var(--green-light)" opacity=".35"/>
    <path d="M0 250 C40 205 120 210 170 240 S 300 230 360 205 S 500 180 540 150"
          fill="none" stroke="var(--string)" stroke-width="1"/>
    <path d="M0 288 C150 308 350 278 540 173 V340 H0 Z" fill="var(--orange)"/>
    <path d="M0 294 C150 314 350 284 540 179 V340 H0 Z" fill="var(--paper)"/>
    <path d="M0 300 C150 320 350 290 540 185 V340 H0 Z" fill="var(--green)"/>
  </svg>
  <h1 class="club-title">Trodza VIP Circle 9</h1>
  <div class="social">
    <span class="social__item">blipster</span>
    <span class="social__item">Chatterly</span>
  </div>
  <div class="brand-name">Trodza</div>
  <div class="photo photo--one" role="img" aria-label="Photo of a white, orange and blue basketball sneaker"></div>
  <div class="photo photo--two" role="img" aria-label="Photo of a white and red high-top sneaker"></div>
  <div class="photo photo--three" role="img" aria-label="Photo of black and red running sneakers"></div>
  <div class="tag tag--one">24%<small>discount</small></div>
  <div class="tag tag--two">24%<small>discount</small></div>
  <div class="web">www.Trodza.com</div>
</section>

<section class="card card--back">
  <svg class="shapes" viewBox="0 0 540 340" preserveAspectRatio="none" aria-hidden="true">
    <path d="M0 50 Q270 35 540 15 V70 Q270 95 0 115 Z" fill="var(--green)"/>
    <path d="M0 310 C160 330 360 300 540 262 V340 H0 Z" fill="var(--orange)"/>
    <path d="M0 316 C160 336 360 306 540 268 V340 H0 Z" fill="var(--paper)"/>
    <path d="M0 322 C160 342 360 312 540 274 V340 H0 Z" fill="var(--green)"/>
  </svg>
  <div class="member-fields">
    <div class="member-fields__row member-fields__row--id">Member ID : <span class="line"></span></div>
    <div class="member-fields__row member-fields__row--name">Member Name : <span class="line"></span></div>
  </div>
  <div class="benefits">
    <h2 class="benefits__title">-: Benefits :-</h2>
    <p>The TRODZA Member Program entitles Members to the following benefits:</p>
    <ol>
      <li><b>a.</b>20% OFF your entire first purchase after you sign up (Limited Time Offer). Certain items are excluded from this offer. Please see stores for details.</li>
      <li><b>b.</b>10% OFF every purchase while being a member. Certain items are excluded from this offer. Please see stores for details.</li>
      <li><b>c.</b>Additional 10% OFF and FREE SHIPPING when an item is out of stock in store but can be shipped to you from another location.</li>
      <li><b>d.</b>Eligible to purchase exclusive items offered to members only. Purchasing of exclusive items is limited to 1 item per member per 30 days. Please see stores for details.</li>
    </ol>
  </div>
  <div class="web">www.Trodza.com</div>
</section>

</body>
</html>
```